Business Card Design

We need a design for business cards for our company. We have a logo. We teach EMT's and we are based out of Virginia. The information that will need to add would be, name, title, phone number, email, address. On the back of the business card would be "We help you, help others"

Target Market(s)

People that want to become EMT's

Colors

Designer to choose colors to be used in the design.

Requirements
Must have
• company logo

```html
<!DOCTYPE html>
<html lang="en">
<head>
<meta charset="utf-8">
<title>Crest Rescue Academy – Business Card</title>
<link rel="stylesheet" href="https://fonts.googleapis.com/css2?family=Montserrat:wght@500;600&family=Oswald:wght@400;500&family=Roboto:wght@400&display=swap">
<style>
  :root {
    --backdrop: #16171a;
    --card: #1f2a36;
    --accent: #e0233f;
    --muted: #8e96a0;
    --light: #b9c0c8;
  }
  * { margin: 0; padding: 0; box-sizing: border-box; }
  html, body { width: 1200px; height: 800px; overflow: hidden; background: var(--backdrop); }
  .canvas { position: relative; width: 1200px; height: 800px; }

  .card {
    position: absolute;
    width: 500px; height: 286px;
    background: var(--card);
    box-shadow: 0 18px 40px rgba(0,0,0,.55);
  }
  .card--front { left: 150px; top: 100px; }
  .card--back  { left: 550px; top: 414px; }

  /* Front */
  .brand {
    position: absolute; left: 0; right: 0; top: 96px;
    display: flex; align-items: center; justify-content: center; gap: 12px;
  }
  .brand__dot { width: 14px; height: 14px; border-radius: 50%; background: var(--accent); }
  .brand__name {
    font-family: "Montserrat", sans-serif; font-weight: 600;
    font-size: 30px; color: var(--accent); letter-spacing: .5px; text-transform: uppercase;
  }
  .tagline {
    position: absolute; left: 0; right: 0; top: 190px; text-align: center;
    font-family: "Montserrat", sans-serif; font-weight: 500;
    font-size: 12px; letter-spacing: 4px; color: var(--muted); text-transform: uppercase;
  }

  /* Back */
  .person { position: absolute; left: 56px; top: 96px; text-align: right; width: 168px; }
  .person__name {
    font-family: "Oswald", sans-serif; font-weight: 500; font-size: 27px; line-height: 1;
    text-transform: uppercase; color: var(--light);
  }
  .person__first { color: var(--accent); }
  .person__title {
    margin-top: 5px;
    font-family: "Oswald", sans-serif; font-weight: 400; font-size: 13px;
    letter-spacing: .5px; text-transform: uppercase; color: var(--muted);
  }
  .divider { position: absolute; left: 238px; top: 92px; width: 1.5px; height: 62px; background: var(--accent); }
  .contacts { position: absolute; left: 252px; top: 92px; list-style: none; }
  .contacts li {
    display: flex; align-items: center; gap: 8px; height: 20px;
    font-family: "Roboto", sans-serif; font-size: 12.5px; color: var(--light);
  }
  .contacts svg { width: 12px; height: 12px; flex: none; }
  .contacts .highlight { color: var(--accent); }
  .address {
    position: absolute; left: 56px; bottom: 34px;
    display: flex; align-items: center; gap: 8px;
    font-family: "Roboto", sans-serif; font-size: 12.5px; color: var(--light);
  }
  .address svg { width: 12px; height: 14px; }
</style>
</head>
<body>
<main class="canvas">
  <section class="card card--front">
    <div class="brand">
      <span class="brand__dot"></span>
      <span class="brand__name">Crest Rescue Academy</span>
    </div>
    <p class="tagline">We help you, help others</p>
  </section>

  <section class="card card--back">
    <div class="person">
      <h1 class="person__name"><span class="person__first">Daniel</span> R. Hayes</h1>
      <p class="person__title">Managing Director</p>
    </div>
    <span class="divider"></span>
    <ul class="contacts">
      <li>
        <svg viewBox="0 0 12 12" aria-hidden="true"><rect x="2.5" y="0.5" width="7" height="11" rx="1.2" fill="none" stroke="var(--accent)" stroke-width="1.2"/><circle cx="6" cy="9.5" r=".7" fill="var(--accent)"/></svg>
        +1 804 555 0192
      </li>
      <li>
        <svg viewBox="0 0 12 12" aria-hidden="true"><rect x="0.5" y="2" width="11" height="8" fill="var(--accent)"/><path d="M0.5 2 L6 6.5 L11.5 2" fill="none" stroke="var(--card)" stroke-width="1"/></svg>
        info@crestrescue.com
      </li>
      <li>
        <svg viewBox="0 0 12 12" aria-hidden="true"><circle cx="6" cy="6" r="5.5" fill="var(--accent)"/><path d="M0.5 6h11M6 .5v11M2 3h8M2 9h8" stroke="var(--card)" stroke-width=".8" fill="none"/><ellipse cx="6" cy="6" rx="2.4" ry="5.5" fill="none" stroke="var(--card)" stroke-width=".8"/></svg>
        <span>www.<span class="highlight">crestrescue</span>.com</span>
      </li>
    </ul>
    <p class="address">
      <svg viewBox="0 0 12 14" aria-hidden="true"><path d="M6 13.5 C2 8.5 1 6.8 1 5 A5 5 0 0 1 11 5 C11 6.8 10 8.5 6 13.5Z" fill="var(--accent)"/><circle cx="6" cy="5" r="1.8" fill="var(--card)"/></svg>
      PO Box 418, 27 Harbor Lane, Richmond
    </p>
  </section>
</main>
</body>
</html>
```